Business Card for Inovative Flexible Packaging Company

Create a business card that is both simple and stricking at the same time.
Preferably only one color (orange) or two colors (black and orange).
Information to print:
Torvalo, Lda
[T] 22 418 6093
[M] 91 326 7041
[F] 22 418 6135
[@] contacto@torvalo-emb.pt
SEDE & ARMAZÉM
Rua Das Figueiras do Monte, 312
Vilarelho
4975-832 Vilarelho - VN Alvora
PORTUGAL
Reason: A lot of the ideas are obvious. I want something different. Inovative. dare to do something eye catching with style.
Business Consumers. Packaging Designers.
Business

```html
<!DOCTYPE html>
<html lang="pt">
<head>
<meta charset="utf-8">
<title>Torvalo, Lda — Cartão de visita</title>
<link rel="stylesheet" href="https://fonts.googleapis.com/css2?family=Arimo:wght@400;700&display=swap">
<style>
  :root {
    --bg: #e9e9e9;
    --paper: #ffffff;
    --orange: #f57c12;
    --orange-deep: #f26a00;
    --orange-soft: #fbb573;
    --ink: #4a4a4a;
    --ink-light: #8a8a8a;
    --facet: #f1f1f1;
  }
  * { box-sizing: border-box; margin: 0; padding: 0; }
  html, body { width: 1200px; height: 795px; overflow: hidden; }
  body {
    background: var(--bg);
    font-family: "Arimo", Arial, sans-serif;
    position: relative;
  }
  .card {
    position: absolute;
    top: 249px;
    width: 520px;
    height: 297px;
    background: var(--paper);
    box-shadow: 0 2px 6px rgba(0,0,0,.12), 0 12px 30px rgba(0,0,0,.08);
    overflow: hidden;
  }
  .card--back { left: 50px; }
  .card--front { left: 630px; }

  /* Back side */
  .facet-texture {
    position: absolute; inset: 0;
    background: linear-gradient(135deg, var(--paper) 0%, var(--facet) 45%, var(--paper) 70%, var(--facet) 100%);
  }
  .brand-stripe {
    position: absolute; left: 0; right: 0; top: 168px;
    height: 9px; background: var(--orange);
  }
  .contact {
    position: absolute; right: 30px; top: 58px;
    text-align: right; color: var(--ink); font-size: 13px; line-height: 1.3;
    white-space: nowrap;
  }
  .contact__company {
    color: var(--orange); font-weight: 700; font-size: 19px; margin-bottom: 4px;
  }
  .contact__row { display: flex; justify-content: flex-end; align-items: center; gap: 5px; }
  .contact__email { font-size: 16px; margin-top: 3px; }
  .icon { width: 11px; height: 11px; fill: var(--orange); flex: none; }
  .address {
    position: absolute; left: 30px; top: 192px;
    color: var(--ink); font-size: 11px; line-height: 1.35; font-style: normal;
    white-space: nowrap;
  }

  /* Front side */
  .pattern-field {
    position: absolute; inset: 0;
    background:
      radial-gradient(ellipse 38% 32% at 52% 48%, var(--paper) 0%, rgba(255,255,255,.85) 55%, rgba(255,255,255,0) 100%),
      linear-gradient(135deg, var(--orange-deep) 0%, var(--orange-soft) 30%, var(--paper) 50%, var(--orange-soft) 72%, var(--orange-deep) 100%);
  }
  .wordmark {
    position: absolute; left: 50%; top: 50%;
    transform: translate(-50%, -55%);
    display: flex; flex-direction: column; align-items: center;
  }
  .wordmark__line { display: flex; align-items: center; gap: 12px; }
  .wordmark__square { width: 38px; height: 38px; background: var(--orange-deep); }
  .wordmark__name {
    color: var(--orange-deep); font-weight: 700; font-size: 54px; letter-spacing: -1px; line-height: 1;
  }
  .wordmark__tagline {
    margin-top: 8px; color: var(--ink-light); font-size: 10px; letter-spacing: 4px;
    padding-left: 50px; white-space: nowrap;
  }
</style>
</head>
<body>

  <section class="card card--back" aria-label="Verso do cartão">
    <div class="facet-texture" role="img" aria-label="Textura geométrica facetada em cinzento muito claro"></div>
    <div class="contact">
      <p class="contact__company">Torvalo, Lda</p>
      <p class="contact__row">22 418 6093</p>
      <p class="contact__row">
        <svg class="icon" viewBox="0 0 12 12" aria-hidden="true"><path d="M3 1 L5 3.5 L4 5 Q5 7 7 8 L8.5 7 L11 9 L9.5 11 Q4.5 10.5 1 3 Z"/></svg>
        91 326 7041
      </p>
      <p class="contact__row">22 418 6135</p>
      <p class="contact__row contact__email">
        <svg class="icon" viewBox="0 0 12 12" aria-hidden="true"><rect x="1" y="3" width="10" height="7" rx="1"/><path d="M1.5 3.5 L6 7 L10.5 3.5" stroke="#fff" stroke-width="1" fill="none"/></svg>
        contacto@torvalo-emb.pt
      </p>
    </div>
    <div class="brand-stripe"></div>
    <address class="address">
      SEDE &amp; ARMAZÉM<br>
      Rua Das Figueiras do Monte, 312 Vilarelho<br>
      4975-832 Vilarelho - VN Alvora<br>
      PORTUGAL
    </address>
  </section>

  <section class="card card--front" aria-label="Frente do cartão">
    <div class="pattern-field" role="img" aria-label="Padrão de polígonos geométricos sobrepostos em tons de laranja"></div>
    <div class="wordmark">
      <div class="wordmark__line">
        <span class="wordmark__square"></span>
        <span class="wordmark__name">torvalo</span>
      </div>
      <p class="wordmark__tagline">FLEXIBLE SOLUTIONS</p>
    </div>
  </section>

</body>
</html>
```